Potential QD Herald Best Seller Poetry Book Cover Contest

I’m penning my first poetry book. It’s entitled “Salt Under Lanterns”
I’m fairly open to creative freedom but I want the cover to without a doubt catch a persons' eye instantly because first impressions are VERY IMPORTANT in the literary world
I tend to lean towards a luxury look and colors like black, gold, rose gold, silver, glitter etc but again I’m open to interpretation
Looking forward to your submissions
those seeking relatable love advice and quotes
modern millenials

```html
<!DOCTYPE html>
<html lang="en">
<head>
<meta charset="utf-8">
<title>Salt Under Lanterns — Book Cover</title>
<link rel="stylesheet" href="https://fonts.googleapis.com/css2?family=Allura&family=Montserrat:wght@500&display=swap">
<style>
  :root {
    --ink-black: #07070b;
    --deep-navy: #0d0e18;
    --gold: #e2d18c;
    --gold-soft: #c9b778;
    --paper-white: #ffffff;
    --author-ink: #111111;
  }
  html, body {
    margin: 0;
    padding: 0;
    width: 800px;
    height: 1200px;
    overflow: hidden;
    background: var(--ink-black);
  }
  .cover {
    position: relative;
    width: 800px;
    height: 1200px;
    overflow: hidden;
    background: linear-gradient(180deg, var(--ink-black) 0%, var(--deep-navy) 55%, var(--ink-black) 80%);
  }
  .gold-dust {
    position: absolute;
    inset: 0;
    background:
      radial-gradient(ellipse 380px 420px at 52% 58%, rgba(226, 209, 140, 0.28), transparent 70%),
      radial-gradient(ellipse 300px 260px at 60% 30%, rgba(226, 209, 140, 0.12), transparent 70%);
  }
  .drip-area {
    position: absolute;
    top: 0;
    left: 0;
    width: 800px;
    height: 400px;
    background: linear-gradient(180deg, var(--gold) 0%, rgba(226, 209, 140, 0.55) 8%, rgba(226, 209, 140, 0.12) 40%, rgba(226, 209, 140, 0) 100%);
  }
  .glitter-floor {
    position: absolute;
    left: 0;
    right: 0;
    bottom: 0;
    height: 300px;
    background: linear-gradient(180deg, rgba(201, 183, 120, 0) 0%, rgba(201, 183, 120, 0.55) 30%, var(--gold-soft) 55%, #d8c78a 100%);
  }
  .title {
    position: absolute;
    left: 0;
    right: 0;
    top: 400px;
    margin: 0;
    text-align: center;
    color: var(--paper-white);
    font-weight: normal;
  }
  .title-script {
    display: block;
    font-family: "Allura", cursive;
    font-size: 150px;
    line-height: 1;
    transform: rotate(-3deg);
  }
  .title-block {
    display: block;
    margin-top: 12px;
    font-family: "Montserrat", sans-serif;
    font-weight: 500;
    font-size: 138px;
    line-height: 1;
    letter-spacing: -3px;
    white-space: nowrap;
  }
  .author {
    position: absolute;
    left: 0;
    right: 0;
    bottom: 50px;
    margin: 0;
    text-align: center;
    font-family: "Allura", cursive;
    font-weight: normal;
    font-size: 88px;
    line-height: 1;
    color: var(--author-ink);
    white-space: nowrap;
  }
</style>
</head>
<body>
<main class="cover">
  <div class="gold-dust" role="img" aria-label="Scattered gold paint flecks across the black background"></div>
  <div class="drip-area" role="img" aria-label="Gold paint dripping down from the top edge"></div>
  <div class="glitter-floor" role="img" aria-label="Gold glitter texture rising from the bottom edge"></div>

  <h1 class="title">
    <span class="title-script">Salt Under</span>
    <span class="title-block">LANTERNS</span>
  </h1>

  <p class="author">Morgan Ellery-Vance</p>
</main>
</body>
</html>
```